New landing page for book

Redesign http://www.quandelfieldworks.com so it looks more cutting edge and perhaps have buttons for the online bookstores.

Also I may soon have a trailer video produced so it Would be great to see an option with space for where a video might go and an option as the site is now without a video. Thanks

Industry/Entity Type

Online

Number of Pages Required

1 page

Colors

Designer to choose colors to be used in the design.

```html
<!DOCTYPE html>
<html lang="en">
<head>
<meta charset="utf-8">
<title>Vardanka — Elias Marrow</title>
<link rel="stylesheet" href="https://fonts.googleapis.com/css2?family=Bebas+Neue&family=Oswald:wght@500;600;700&family=Open+Sans:wght@400;600;700&family=Roboto+Slab:wght@700&display=swap">
<style>
  :root{
    --orange:#f07c1b;
    --orange-light:#f8a23a;
    --gold:#e2a552;
    --bronze:#8a5a36;
    --dark:#141414;
    --teal:#2f5f57;
    --teal-dark:#234a44;
    --ink:#3b3b3b;
    --heading:#3c3f42;
    --card:#e2e3e4;
    --white:#ffffff;
  }
  *{box-sizing:border-box;margin:0;padding:0}
  html,body{width:1200px;height:2946px;overflow:hidden;background:var(--dark)}
  body{font-family:"Open Sans",sans-serif;position:relative}
  .abs{position:absolute}

  /* Hero */
  .hero{position:absolute;left:0;top:0;width:1200px;height:678px;
    background:radial-gradient(ellipse at 60% 40%,#3a3a3a 0%,#1c1c1c 55%,#0e0e0e 100%)}
  .brand{left:98px;top:22px;font-family:"Oswald",sans-serif;font-weight:700;font-size:46px;line-height:1;color:var(--orange)}
  .brand-author{left:150px;top:74px;font-family:"Oswald",sans-serif;font-weight:600;font-size:13px;letter-spacing:1px;color:var(--orange)}
  .nav{right:100px;top:36px;display:flex;gap:40px;font-family:"Oswald",sans-serif;font-weight:600;font-size:23px;letter-spacing:1px;color:var(--orange)}
  .nav span small{font-size:12px;margin-left:8px;vertical-align:middle}
  .hero-kicker{left:98px;top:160px;width:410px;font-family:"Bebas Neue",sans-serif;font-weight:400;font-size:52px;line-height:1;color:var(--gold);white-space:nowrap}
  .hero-title{left:98px;top:210px;width:410px;font-family:"Bebas Neue",sans-serif;font-weight:400;font-size:86px;line-height:1;color:var(--orange-light);white-space:nowrap}
  .hero-buy{left:98px;top:320px;font-family:"Roboto Slab",serif;font-weight:700;font-size:38px;letter-spacing:3px;color:var(--bronze)}
  .stores{left:98px;top:387px;display:grid;grid-template-columns:162px 202px;column-gap:11px;row-gap:16px}
  .store{height:55px;border:2px solid #777;border-radius:14px;background:#000;color:var(--white);
    display:flex;align-items:center;justify-content:center;gap:10px;font-family:"Open Sans",sans-serif;font-weight:700;font-size:20px}
  .store i{width:18px;height:18px;border-radius:50%;background:var(--white);display:block}
  .cover{border-radius:4px}
  .hero-cover{left:560px;top:100px;width:600px;height:578px;
    background:linear-gradient(135deg,#6b4a2c 0%,#2c4f47 55%,#1b332e 100%)}

  .stripe{position:absolute;left:0;width:1200px;
    background:repeating-linear-gradient(45deg,#1a1a1a 0 4px,#262626 4px 8px)}

  /* Story */
  .story{position:absolute;left:0;top:727px;width:1200px;height:1148px;
    background:radial-gradient(ellipse at 50% 45%,#fbfbfb 0%,#eeeeee 60%,#cfcfcf 100%)}
  .story-h{left:0;top:90px;width:1200px;text-align:center;font-family:"Oswald",sans-serif;font-weight:700;font-size:56px;line-height:1;color:var(--heading)}
  .rule{height:4px;background:var(--heading)}
  .story-sub{left:0;top:162px;width:1200px;text-align:center;font-family:"Oswald",sans-serif;font-weight:700;font-size:40px;line-height:50px;color:var(--heading)}
  .pill{left:124px;top:304px;width:952px;height:89px;border-radius:45px;background:var(--teal);
    box-shadow:0 4px 8px rgba(0,0,0,.35);display:flex;align-items:center;justify-content:center;text-align:center;
    font-family:"Open Sans",sans-serif;font-weight:700;font-size:18.5px;line-height:23px;color:var(--white);padding:0 60px}
  .body{left:150px;top:430px;width:900px;text-align:center;font-size:16.5px;line-height:23px;color:var(--ink)}
  .body p{margin-bottom:23px}
  .pitch{left:124px;top:740px;width:500px;font-family:"Oswald",sans-serif;font-weight:500;font-size:25px;line-height:36px;color:var(--teal-dark)}
  .story-cover{left:650px;top:690px;width:510px;height:430px;
    background:linear-gradient(160deg,#6b4a2c 0%,#2c4f47 55%,#1b332e 100%)}

  .btn{display:flex;align-items:center;justify-content:space-between;padding:0 12px 0 48px;border-radius:44px;
    background:linear-gradient(#f9a440,#e8700f);box-shadow:0 4px 6px rgba(0,0,0,.35);
    font-family:"Roboto Slab",serif;font-weight:700;color:var(--white);letter-spacing:1px}
  .btn .cart{width:56px;height:56px;border-radius:50%;background:rgba(255,255,255,.25);display:flex;align-items:center;justify-content:center}
  .story-btn{left:124px;top:946px;width:367px;height:85px;font-size:40px}

  /* Reviews */
  .reviews{position:absolute;left:0;top:1921px;width:1200px;height:475px;background:#ececec}
  .rev-h{left:0;top:50px;width:1200px;text-align:center;font-family:"Oswald",sans-serif;font-weight:700;font-size:48px;line-height:1;color:var(--heading)}
  .rev-tag{left:0;top:120px;width:1200px;text-align:center;font-size:13px;letter-spacing:1px;color:#666}
  .card{top:161px;height:177px;background:var(--card);padding:30px 26px;text-align:center;font-size:13.5px;line-height:20px;color:#444}
  .who{top:365px;display:flex;align-items:center;gap:22px;font-family:"Oswald",sans-serif;font-weight:600;font-size:19px;color:var(--orange)}
  .who i{width:66px;height:66px;border-radius:50%;background:linear-gradient(#8a7866,#4a4e55);border:3px solid #fff;display:block}

  /* Release */
  .release{position:absolute;left:0;top:2396px;width:1200px;height:452px;
    background:linear-gradient(#1b1b1b,#2a2a2a 70%,#3a3a3a)}
  .rel-h{left:118px;top:40px;font-family:"Oswald",sans-serif;font-weight:700;font-size:124px;line-height:1;color:#b97a4b}
  .rel-date{left:124px;top:180px;font-family:"Oswald",sans-serif;font-weight:700;font-size:56px;line-height:1;color:var(--orange)}
  .rel-mail{left:124px;top:252px;font-size:32px;color:var(--white)}
  .rel-btn{left:124px;top:314px;width:357px;height:79px;font-size:38px}
  .rel-cover{left:650px;top:10px;width:510px;height:432px;
    background:linear-gradient(135deg,#6b4a2c 0%,#2c4f47 55%,#1b332e 100%)}

  .copy{left:0;top:2848px;width:1200px;height:98px;display:flex;align-items:center;justify-content:center;
    font-family:"Oswald",sans-serif;font-weight:500;font-size:25px;color:var(--white)}
</style>
</head>
<body>

<header class="hero">
  <div class="abs brand">Vardanka</div>
  <div class="abs brand-author">ELIAS MARROW</div>
  <nav class="abs nav"><span>BUY NOW!<small>▼</small></span><span>CONTACT</span></nav>
  <div class="abs cover hero-cover" role="img" aria-label="Stack of Vardanka books by Elias Marrow, cover showing an armed agent before the Capitol"></div>
  <div class="abs hero-kicker">INTERNATIONAL FINANCIAL</div>
  <div class="abs hero-title">CRIME THRILLER</div>
  <div class="abs hero-buy">BUY NOW</div>
  <div class="abs stores">
    <div class="store"><i></i>Brightshelf</div>
    <div class="store">Page &amp; Lantern</div>
    <div class="store">Northplay</div>
    <div class="store"><i></i>Readwell</div>
    <div class="store"><i></i>Lumo</div>
    <div class="store">Inkloft</div>
  </div>
</header>

<div class="stripe" style="top:678px;height:49px"></div>

<section class="story">
  <div class="abs rule" style="left:98px;top:116px;width:225px"></div>
  <div class="abs rule" style="left:874px;top:116px;width:225px"></div>
  <h1 class="abs story-h">ATMS HAVE SHUTTERED.</h1>
  <h2 class="abs story-sub">STOCK MARKETS HAVE GONE HAYWIRE. CAN ONE OPERATIVE<br>STOP A DEADLY BAND OF CRIMINALS BEFORE IT IS TOO LATE?</h2>
  <div class="abs pill">WHEN ANTON KELLER IS ASKED TO INVESTIGATE A DEVASTATING CYBER-ATTACK, HE IS DRAWN INTO A CONSPIRACY THAT THREATENS NOT ONLY HIS OWN LIFE, BUT THE ENTIRE UNITED STATES' ECONOMY...</div>
  <div class="abs body">
    <p>German intelligence operative Anton Keller has been asked to investigate the cyber crime gang who sparked massive unrest in Kenya by taking over electronic transactions. But as he digs deeper, a wiretap on hacker communications reveals this is only the beginning.</p>
    <p>Vardanka, a shadowy criminal cabal, has launched a massive cyber attack on the United States.</p>
    <p>Taking off for Washington, Keller unexpectedly teams up with American gun for hire, Nils Haverford, and dives head-first into a massive conspiracy that reaches all the way up to the very top of the U.S. Government.</p>
    <p>Stock markets have gone haywire. ATMs have shuttered. And Anton Keller is about to come face to face with the men he is sent to find....</p>
  </div>
  <p class="abs pitch">From the deadly streets of Budapest to the equally perilous corridors of Washington, Vardanka is an action-packed, compulsive thriller that depicts a financial scam terrifyingly close to reality.</p>
  <div class="abs cover story-cover" role="img" aria-label="Vardanka paperback lying at an angle, cover with armed agent and city skyline"></div>
  <a class="abs btn story-btn">BUY NOW
    <span class="cart"><svg width="32" height="28" viewBox="0 0 32 28" fill="none" stroke="#fff" stroke-width="3" stroke-linejoin="round"><path d="M1 3h5l4 15h16l4-11H8"/><circle cx="12" cy="24" r="2" fill="#fff"/><circle cx="24" cy="24" r="2" fill="#fff"/></svg></span>
  </a>
</section>

<div class="stripe" style="top:1875px;height:46px"></div>

<section class="reviews">
  <div class="abs rule" style="left:98px;top:74px;width:225px"></div>
  <div class="abs rule" style="left:874px;top:74px;width:225px"></div>
  <h2 class="abs rev-h">IN THE WORDS OF REVIEWERS</h2>
  <div class="abs rev-tag">WHAT PEOPLE SAY</div>
  <blockquote class="abs card" style="left:98px;width:318px">"Marrow's fast-paced novel is reinforced by its skilled characters"</blockquote>
  <blockquote class="abs card" style="left:446px;width:312px">"In a world ravaged by international turmoil and uncertainty for the future, author Elias Marrow presents Vardanka, an intense and politically charged novel that is both timely and terrifying."</blockquote>
  <blockquote class="abs card" style="left:788px;width:312px">"I give Vardanka by Elias Marrow a definite four out of four stars. The action is fast paced so that it keeps you wanting to see what comes next."</blockquote>
  <div class="abs who" style="left:98px"><i role="img" aria-label="Reviewer avatar"></i>HALVARD REVIEWS</div>
  <div class="abs who" style="left:446px"><i role="img" aria-label="Reviewer avatar"></i>READER</div>
  <div class="abs who" style="left:788px"><i role="img" aria-label="Reviewer avatar"></i>READERS CIRCLE</div>
</section>

<section class="release">
  <div class="abs cover rel-cover" role="img" aria-label="Stack of Vardanka books on a wooden floor"></div>
  <div class="abs rel-h">RELEASED</div>
  <div class="abs rel-date">SEPTEMBER 22, 2017</div>
  <div class="abs rel-mail">help@quandelfieldworks.com</div>
  <a class="abs btn rel-btn">BUY NOW
    <span class="cart"><svg width="32" height="28" viewBox="0 0 32 28" fill="none" stroke="#fff" stroke-width="3" stroke-linejoin="round"><path d="M1 3h5l4 15h16l4-11H8"/><circle cx="12" cy="24" r="2" fill="#fff"/><circle cx="24" cy="24" r="2" fill="#fff"/></svg></span>
  </a>
</section>

<footer class="stripe abs copy">© COPYRIGHT 2017 ELIAS MARROW - ALL RIGHTS RESERVED</footer>

</body>
</html>
```